Roll-Up Banner für Glückswebsite
Das war eine großartige Zusammenarbeit und unserem sehr knappen Zeitplan extrem entgegenkommend. Das design ist gleichzeitig seriös und trotzdem jung und dynamisch! Perfekt!
Zielgruppe
Die Website, www.freudenpfad.de ermöglicht es jedem Interessierten kostenlos mehr über das eigene Lebensglück, persönliche Stärken, und die eigene Lebenszufriedenheit herauszufinden. Interessierte können online Fragebögen ausfüllen, und erhalten neben einer detaillierten Rückmeldung über die eigenen Möglichkeiten und Stärken, Hinweise dazu, wie Sie an Ihrem eigenen Potenzial arbeiten können. Es handelt sich um ein Kooperationsprojekt der Nordischen Vereinigung für Heitere Seelenkunde der Uni Wendelstein, der HK-Lindau, der Health Academy Marbach und der Uni Falkenried. Zielgruppe für das Banner sind Menschen, die selbst mit Klienten im Kontext der Positiven Psychologie arbeiten oder Menschen, die sich Ihrem eigenen Lebensglück zuwenden wollen.
Aufgabenstellung
Es handelt sich um ein Roll-up Banner in den Maßen 1m Breite und 2 Meter Höhe.
Das Banner sollte so angelegt sein, dass es interessierten Besuchern auf Kongressen vermittelt, was es mit der Seite Freudenpfad.de auf sich hat. Also wissenschaftlich evaluierte kostenfreie online-Fragebögen, die Menschen dabei helfen Ihre eigenen Stärken und Potenziale zu entdecken und dem eigenen Glück näher zu kommen.
Es sollte außerdem das Logo der NVHS darauf zu sehen sein, sowie kleiner die Logos der Forschungskooperationspartner, HK-Lindau, Uni Wendelstein, Uni Falkenried, Health Academy Marbach.
Die Farben sollten zum Logo der NVHS passen.

```html
<!DOCTYPE html>
<html lang="de">
<head>
<meta charset="utf-8">
<title>Freudenpfad.de – Roll-Up</title>
<link href="https://fonts.googleapis.com/css2?family=Fira+Sans+Extra+Condensed:wght@600&family=Open+Sans:wght@700&family=Source+Sans+3:wght@400;600&display=swap" rel="stylesheet">
<style>
  :root {
    --teal: #19a98b;
    --cyan: #2bb5c8;
    --green: #8fc03c;
    --mint: #22a98c;
    --navy: #1a2e5e;
    --ink: #1f1f1f;
    --white: #ffffff;
    --wall-light: #d8d5d1;
    --wall-dark: #b3afab;
  }
  html, body { margin: 0; padding: 0; overflow: hidden; }
  body { width: 1200px; height: 2400px; background: var(--white); position: relative; font-family: "Source Sans 3", sans-serif; color: var(--ink); }
  .banner { position: absolute; inset: 0; overflow: hidden; }

  .brand { position: absolute; left: 135px; top: 290px; }
  .brand-mark { display: flex; align-items: center; gap: 14px; }
  .brand-dot { width: 28px; height: 28px; border-radius: 50%; background: var(--teal); }
  .brand-name { font-weight: 600; font-size: 46px; color: var(--navy); letter-spacing: 3px; line-height: 1; }
  .brand-sub { margin-top: 14px; font-size: 19px; line-height: 24px; color: var(--navy); }
  .brand-sub strong { font-weight: 600; }

  .hero { position: absolute; left: 387px; top: 0; width: 813px; height: 447px;
    background: linear-gradient(60deg, var(--teal) 0%, var(--teal) 45%, var(--cyan) 100%); color: var(--white); }
  .hero-title { position: absolute; left: 46px; top: 138px; margin: 0; font-family: "Fira Sans Extra Condensed", sans-serif; font-weight: 600; font-size: 112px; line-height: 1; letter-spacing: -1px; }
  .hero-sub { position: absolute; left: 46px; top: 278px; margin: 0; font-size: 41px; line-height: 60px; }

  .gallery { position: absolute; left: 56px; top: 447px; width: 1090px; height: 1092px; background: var(--white); }
  .gallery-grid { position: absolute; left: 12px; top: 15px; width: 1071px; height: 1064px;
    display: grid; grid-template-columns: repeat(5, 1fr); grid-template-rows: repeat(5, 1fr); gap: 4px; }
  .portrait { background:
      radial-gradient(ellipse 38% 34% at 50% 42%, var(--skin, #c99a7c) 0%, transparent 100%),
      linear-gradient(to bottom, var(--wall-light) 0%, var(--wall-dark) 62%, var(--c) 82%, var(--c) 100%); }

  .cta { position: absolute; left: 387px; top: 1539px; width: 813px; height: 606px;
    background: linear-gradient(20deg, var(--green) 0%, var(--mint) 55%, var(--teal) 100%); color: var(--white); }
  .cta-title { position: absolute; left: 56px; top: 46px; margin: 0; font-family: "Open Sans", sans-serif; font-weight: 700; font-size: 58px; line-height: 76px; letter-spacing: -0.5px; }
  .cta-steps { position: absolute; left: 56px; top: 240px; margin: 0; padding: 0; list-style: none; font-size: 42.5px; line-height: 51px; }
  .cta-steps li::before { content: "» "; }

  .partners-label { position: absolute; left: 63px; top: 2162px; font-size: 24px; }
  .partner { position: absolute; display: flex; align-items: center; gap: 10px; font-size: 23px; color: var(--ink); white-space: nowrap; }
  .partner-square { width: 24px; height: 24px; background: var(--teal); }
  .p1 { left: 63px; top: 2296px; }
  .p2 { left: 410px; top: 2296px; }
  .p3 { left: 643px; top: 2296px; }
  .p4 { left: 941px; top: 2296px; }
</style>
</head>
<body>
<div class="banner">
  <div class="brand">
    <div class="brand-mark"><span class="brand-dot"></span><span class="brand-name">NVHS</span></div>
    <div class="brand-sub">Nordische Vereinigung für<br><strong>Heitere Seelenkunde</strong></div>
  </div>

  <header class="hero">
    <h1 class="hero-title">Freudenpfad.de</h1>
    <p class="hero-sub">Wissenschaftlich evaluierte kostenfreie<br>online-Fragebögen.</p>
  </header>

  <div class="gallery">
    <div class="gallery-grid" role="img" aria-label="Raster aus 25 Porträtfotos lachender Menschen unterschiedlichen Alters und Herkunft vor hellgrauem Hintergrund">
      <div class="portrait" style="--c:#a8a2c4;--skin:#6b4632"></div>
      <div class="portrait" style="--c:#9fc0de;--skin:#d9a98c"></div>
      <div class="portrait" style="--c:#d9a23a;--skin:#d7a58a"></div>
      <div class="portrait" style="--c:#5f86ad;--skin:#c9977a"></div>
      <div class="portrait" style="--c:#4a4d57;--skin:#d6a88e"></div>

      <div class="portrait" style="--c:#e2b21e;--skin:#cf9c7f"></div>
      <div class="portrait" style="--c:#8fc1dd;--skin:#e0b49a"></div>
      <div class="portrait" style="--c:#e2b62c;--skin:#d7a68a"></div>
      <div class="portrait" style="--c:#dedbd6;--skin:#dcb39c"></div>
      <div class="portrait" style="--c:#2f8fd0;--skin:#d8a98c"></div>

      <div class="portrait" style="--c:#8d8f93;--skin:#ddb29a"></div>
      <div class="portrait" style="--c:#f0c21a;--skin:#4e3223"></div>
      <div class="portrait" style="--c:#2c84b3;--skin:#d6aa94"></div>
      <div class="portrait" style="--c:#2e6fc4;--skin:#c99878"></div>
      <div class="portrait" style="--c:#dca52a;--skin:#d6a487"></div>

      <div class="portrait" style="--c:#5a3a86;--skin:#c99a80"></div>
      <div class="portrait" style="--c:#3a6ea8;--skin:#d8a98c"></div>
      <div class="portrait" style="--c:#7d8fae;--skin:#5a3a28"></div>
      <div class="portrait" style="--c:#3d8ccf;--skin:#e0b59b"></div>
      <div class="portrait" style="--c:#a9c8e6;--skin:#dcae92"></div>

      <div class="portrait" style="--c:#c8454e;--skin:#c8906e"></div>
      <div class="portrait" style="--c:#d08a2a;--skin:#d4a27f"></div>
      <div class="portrait" style="--c:#3a7cc0;--skin:#dcae92"></div>
      <div class="portrait" style="--c:#8f86c4;--skin:#d1a088"></div>
      <div class="portrait" style="--c:#8ec0e0;--skin:#e0b49a"></div>
    </div>
  </div>

  <section class="cta">
    <h2 class="cta-title">Entdecken Sie sich und<br>Ihre Stärken</h2>
    <ul class="cta-steps">
      <li>kostenfrei registrieren</li>
      <li>online Fragebogen ausfüllen</li>
      <li>persönliche Rückmeldungen erhalten</li>
    </ul>
  </section>

  <div class="partners-label">Forschungskooperation:</div>
  <div class="partner p1"><span class="partner-square"></span>HK-Lindau</div>
  <div class="partner p2"><span class="partner-square"></span>Uni Wendelstein</div>
  <div class="partner p3"><span class="partner-square"></span>Health Academy Marbach</div>
  <div class="partner p4"><span class="partner-square"></span>Uni Falkenried</div>
</div>
</body>
</html>
```